Political Candidate Newspaper Advertisement

I would like a newspaper ad for my campaign for election to City Council. The banner ad is 10 cm high x 26.2 cm wide. The banner will contain a photo and the following text (or words to similar effect):
VOTE
DENNIS HALE
COMO BEACH
For a
SAFE
CARING
CONNECTED
COMMUNITY
Lifetime commitment to local clubs, charities and international aid
Local business owner
Founder of Open-Gate Week
Councillor, Mediator, B.Sc., MBA
The Councillor you know and can call for help
Respects our heritage and our future
Listens to the wisdom and needs of older residents
Promotes more young people
Protects our South Perth environment
Authorised by Dennis Hale 5/348 Kelby Rd, Como. 9317 2864
I use MS Publisher and PhotoShop so I'd like the product to be in a form I can use. After ther banner ad is done, and if it is good, I wish to pay the designer to use the same theme to produce another newspaper ad, a brochure and a poster.
My simple version is attached. A photo is also attached.
I'm hoping you do better.
18-80 years old
Business
- simple fonts
- A TICK somewhere around the word Vote would be good.
Mention of www.fairlandward.notepage.net if possible, perhaps at the bottom of the page, along with the Authorised by ... text.

```html
<!DOCTYPE html>
<html lang="en">
<head>
<meta charset="utf-8">
<title>Vote Dennis Hale – Como Beach</title>
<link rel="stylesheet" href="https://fonts.googleapis.com/css2?family=Nunito:wght@900&family=Arimo:wght@400;700&display=swap">
<style>
  :root {
    --frame-light: #f4f4f4;
    --frame-mid: #b9b9b9;
    --frame-dark: #6a6a6a;
    --panel-top: #2a2a2a;
    --panel-mid: #3a3a3a;
    --panel-bottom: #1e1e1e;
    --headline-light: #ffffff;
    --headline-shade: #bdbdbd;
    --lime: #b8ff1a;
    --body-text: #ffffff;
    --photo-light: #c9a78e;
    --photo-dark: #2d2d33;
    --badge-blue: #1f78c8;
    --badge-edge: #c2308f;
    --badge-text: #0d1f33;
  }
  * { margin: 0; padding: 0; box-sizing: border-box; }
  html, body { width: 1200px; height: 458px; overflow: hidden; background: #ffffff; }
  .banner {
    position: relative; width: 1200px; height: 458px;
    background: linear-gradient(90deg, var(--frame-dark) 0%, var(--frame-light) 25%, var(--frame-mid) 50%, var(--frame-light) 75%, var(--frame-dark) 100%);
  }
  .panel {
    position: absolute; left: 14px; top: 22px; width: 1174px; height: 424px;
    background: linear-gradient(180deg, var(--panel-top) 0%, var(--panel-mid) 45%, var(--panel-bottom) 100%);
  }
  .headline {
    position: absolute; left: 14px; top: 22px; width: 290px; text-align: center;
    font-family: "Nunito", sans-serif; font-weight: 900; font-size: 38px; line-height: 57px;
    letter-spacing: 1px;
    background: linear-gradient(180deg, var(--headline-light) 30%, var(--headline-shade) 100%);
    -webkit-background-clip: text; background-clip: text; color: transparent;
  }
  .headline span { display: block; }
  .slogan {
    position: absolute; left: 14px; top: 216px; width: 290px; text-align: center;
    font-family: "Arimo", sans-serif; font-weight: 700; font-size: 22px; line-height: 46px;
    color: var(--lime);
  }
  .slogan span { display: block; }
  .points {
    position: absolute; top: 44px;
    font-family: "Arimo", sans-serif; font-size: 20.5px; line-height: 32.4px;
    color: var(--body-text);
  }
  .points span { display: block; white-space: nowrap; }
  .points--record { left: 332px; }
  .points--promise { left: 641px; }
  .portrait {
    position: absolute; left: 900px; top: 40px; width: 288px; height: 406px;
    background: radial-gradient(ellipse at 48% 28%, var(--photo-light) 0%, #8a7466 35%, var(--photo-dark) 70%);
    border-radius: 120px 120px 0 0;
  }
  .authorised {
    position: absolute; left: 899px; top: 405px; width: 145px; height: 41px;
    background: var(--badge-blue); border: 2px solid var(--badge-edge); border-radius: 5px;
    font-family: "Arimo", sans-serif; font-size: 8.5px; line-height: 11px;
    color: var(--badge-text); text-align: center; padding-top: 7px;
  }
</style>
</head>
<body>
<div class="banner">
  <div class="panel"></div>

  <h1 class="headline">
    <span>VOTE</span>
    <span>DENNIS HALE</span>
    <span>COMO BEACH</span>
  </h1>

  <p class="slogan">
    <span>For a</span>
    <span>SAFE</span>
    <span>CARING</span>
    <span>CONNECTED</span>
    <span>COMMUNITY</span>
  </p>

  <p class="points points--record">
    <span>A lifetime of commit-</span>
    <span>ment to local clubs,</span>
    <span>charities and interna-</span>
    <span>tional aid</span>
    <span>Local business owner</span>
    <span>Founder of Open-Gate Week</span>
    <span>Councillor, Mediator,</span>
    <span>B.App.Sc., MBA, GAICD</span>
    <span>Drive and energy to</span>
    <span>see things through</span>
    <span>Protects our South</span>
    <span>Perth environment</span>
  </p>

  <p class="points points--promise">
    <span>The Councillor you</span>
    <span>know, can call for help</span>
    <span>and who listens</span>
    <span>Respects our heritage</span>
    <span>whilst considering</span>
    <span>future needs</span>
    <span>Listens to the wisdom</span>
    <span>and needs of older</span>
    <span>residents</span>
    <span>Promotes involvement</span>
    <span>of more young people</span>
    <span>I really enjoy what I do</span>
  </p>

  <div class="portrait" role="img" aria-label="Portrait photo of the candidate in a dark suit, light shirt and patterned tie"></div>

  <div class="authorised">
    Authorised by Dennis Hale<br>
    5/348 Kelby Rd, Como. 9317 2864
  </div>
</div>
</body>
</html>
```